Medical Device - Case Study Template

We need a TEMPLATE that we can reuse to write various case studies about the medical equipment solutions we provide. It will be a double sided letter sized with a modern design that conveys a feeling of expertise, innovation and highly personable service AND be consistent with the brand guide. The content will be divided into a few sections:

- Situation (200-250 words)
- Challenge (100-120 words)
- Solution (100-120 words)
- Results (100-120 words)
- Conclusion (100-120 words)

Additionally, there will need to be a call to action, inviting people to send an email for more information and a short "About Valtu" section (approx. 40 words).

For device picture placeholders, feel free to use any random small benchtop medical device.

```html
<!DOCTYPE html>
<html lang="en">
<head>
<meta charset="UTF-8">
<title>Valtu – Case Study Template</title>
<link href="https://fonts.googleapis.com/css2?family=Montserrat:wght@600;700;800&family=Open+Sans:wght@400;600&display=swap" rel="stylesheet">
<style>
  :root {
    --orange: #f26f21;
    --blue: #2f8fc9;
    --navy: #1d5f8f;
    --ink: #4a4f55;
    --paper: #ffffff;
    --backdrop: #e9eaec;
  }
  * { box-sizing: border-box; margin: 0; padding: 0; }
  html, body { width: 900px; height: 1200px; overflow: hidden; }
  body { background: var(--backdrop); font-family: 'Open Sans', sans-serif; color: var(--ink); position: relative; }

  .sheet {
    position: absolute; top: 322px; width: 430px; height: 556px;
    background: var(--paper); overflow: hidden;
    box-shadow: 0 4px 14px rgba(0,0,0,.12);
  }
  .sheet--front { left: 13px; }
  .sheet--back { left: 457px; }

  .abs { position: absolute; }
  .photo { position: absolute; }

  /* brand */
  .brand { left: 20px; top: 14px; display: flex; align-items: center; gap: 7px; }
  .brand-dot { width: 14px; height: 14px; border-radius: 50%; background: var(--orange); }
  .brand-name { font-family: 'Montserrat', sans-serif; font-weight: 700; font-size: 22px; color: var(--orange); line-height: 1; }
  .brand-tag { left: 41px; top: 38px; font-size: 8px; color: var(--ink); letter-spacing: .3px; }

  .headline { font-family: 'Montserrat', sans-serif; font-weight: 800; color: #fff; font-size: 20px; }
  .body { font-size: 7.4px; line-height: 1.5; }
  .body--light { color: #fff; }

  .section-title { font-family: 'Montserrat', sans-serif; font-weight: 800; font-size: 12px; color: var(--blue); letter-spacing: .5px; }
  .tag {
    display: inline-block; font-family: 'Montserrat', sans-serif; font-weight: 800;
    font-size: 10px; color: #fff; padding: 3px 12px; letter-spacing: .5px;
  }
  .tag--orange { background: var(--orange); }
  .tag--blue { background: var(--blue); }

  .cta { background: var(--blue); color: #fff; padding: 10px 12px; }
  .cta-title { font-family: 'Montserrat', sans-serif; font-weight: 800; font-size: 15px; line-height: 1.1; }
  .cta-mail { font-size: 8px; color: #ffd2b5; font-weight: 600; margin-top: 6px; }
  .cta-call { font-family: 'Montserrat', sans-serif; font-weight: 700; font-size: 11px; margin-top: 3px; }

  .footer { left: 0; right: 0; bottom: 0; height: 34px; display: flex; align-items: center; justify-content: center; font-size: 9px; color: #fff; }
  .footer--blue { background: var(--blue); }
  .footer--orange { background: var(--orange); }
  .footer-url { font-weight: 600; margin-left: 4px; }
  .footer--blue .footer-url { color: #ffc39c; }
</style>
</head>
<body>

<!-- Front side -->
<section class="sheet sheet--front">
  <div class="abs brand"><span class="brand-dot"></span><span class="brand-name">Valtu</span></div>
  <div class="abs brand-tag">Medical Technology</div>

  <div class="photo" role="img" aria-label="Operating room with a cart-mounted ultrasound system"
       style="left:0; top:60px; width:430px; height:190px; background:linear-gradient(120deg,#9fc6e2 0%,#dfeef8 45%,#7fa9c9 100%);"></div>

  <svg class="abs" style="left:0; top:220px;" width="430" height="130" viewBox="0 0 430 130" aria-hidden="true">
    <polygon points="0,22 430,0 430,130 0,130" fill="var(--orange)"/>
  </svg>
  <h1 class="abs headline" style="left:20px; top:250px;">What is LOREM IPSUM?</h1>
  <p class="abs body body--light" style="left:20px; top:280px; width:390px;">
    Valtu partners with clinics and hospitals to select, install and service diagnostic equipment. This case study shows how our team helped a regional care centre modernise its imaging suite, cut waiting times and give staff tools they trust every single day.
  </p>

  <h2 class="abs section-title" style="left:20px; top:362px;">SITUATION</h2>
  <p class="abs body" style="left:20px; top:382px; width:188px;">
    The centre relied on ageing ultrasound units that broke down often and slowed routine scans. Patients waited weeks for appointments, and technicians spent hours each week working around faults instead of caring for people.
  </p>

  <div class="abs cta" style="left:222px; top:358px; width:190px; height:92px;">
    <div class="cta-title">MAIL US MORE<br>INFORMATION</div>
    <div class="cta-mail">info@valtumedical.com</div>
    <div class="cta-call">CALL - 555 0142 180</div>
  </div>

  <div class="photo" role="img" aria-label="Compact benchtop medical device"
       style="left:20px; top:460px; width:90px; height:50px; background:linear-gradient(180deg,#f1f3f5,#c9d2da);"></div>
  <p class="abs body" style="left:120px; top:466px; width:292px;">
    About Valtu: we deliver trusted medical technology with personal service, from first consultation to long-term support.
  </p>

  <div class="abs footer footer--blue">visit us today:<span class="footer-url">www.valtumedical.com</span></div>
</section>

<!-- Back side -->
<section class="sheet sheet--back">
  <div class="photo" role="img" aria-label="Angled close-up of ultrasound equipment in a bright clinic"
       style="left:0; top:0; width:430px; height:205px; background:linear-gradient(135deg,#e8f1f8 0%,#a9c9e2 50%,#eef4f9 100%);"></div>

  <div class="abs" style="left:18px; top:222px; width:190px;">
    <span class="tag tag--orange">CHALLENGE</span>
    <p class="body" style="margin-top:8px;">The team needed new equipment without closing rooms or disrupting patient schedules, all within a fixed annual budget and a tight timeline.</p>
  </div>
  <div class="abs" style="left:18px; top:318px; width:190px;">
    <span class="tag tag--blue">RESULTS</span>
    <p class="body" style="margin-top:8px;">Scan capacity rose by a third, downtime fell sharply and patient waiting lists shrank within the first three months.</p>
  </div>
  <div class="abs" style="left:18px; top:410px; width:190px;">
    <span class="tag tag--orange">SOLUTION</span>
    <p class="body" style="margin-top:8px;">A phased rollout, hands-on training and responsive service gave the centre reliable imaging and a partner it can count on.</p>
  </div>

  <div class="abs" style="left:226px; top:222px; width:186px;">
    <span class="tag tag--blue">SOLUTION</span>
    <p class="body" style="margin-top:8px;">Valtu mapped each room, recommended compact benchtop and cart units, and scheduled installation over quiet weekends so every department kept running.</p>
  </div>
  <div class="photo" role="img" aria-label="Portable ultrasound unit on a wheeled stand"
       style="left:280px; top:330px; width:110px; height:170px; background:linear-gradient(180deg,#f4f6f8,#cdd6de);"></div>

  <div class="abs footer footer--orange">visit us today:<span class="footer-url">www.valtumedical.com</span></div>
</section>

</body>
</html>
```